Law firm for traffic law - company portfolio

Company folder with logo and picture on the front. On the back only the imprint in DinA4 format. The following folders are ordered
https://www.falzhaus-kremvel.de/mappe-fuer-din-a4-2teilig-mit-2-laschen-40-farbig-aussseite-bedruck-mit-mattfolie-kaschiert.html#content-view

```html
<!DOCTYPE html>
<html lang="de">
<head>
<meta charset="utf-8">
<title>VERIDAX – Unternehmensmappe</title>
<link href="https://fonts.googleapis.com/css2?family=Montserrat:wght@400;600;700;800&display=swap" rel="stylesheet">
<style>
:root{
  --navy:#1d3d5e;
  --navy-dark:#142c45;
  --orange:#f2a320;
  --ink:#2a2f36;
  --muted:#6b737c;
  --paper:#ffffff;
  --stage:#e6e7e9;
}
*{box-sizing:border-box;margin:0;padding:0}
html,body{width:1200px;height:2896px;overflow:hidden}
body{background:var(--stage);font-family:"Montserrat",Arial,sans-serif;color:var(--ink);position:relative}
.sheet{position:absolute;background:var(--paper);overflow:hidden;box-shadow:0 2px 10px rgba(0,0,0,.08)}
.abs{position:absolute}
.brand{font-weight:800;color:var(--navy);letter-spacing:3px;display:flex;align-items:center;gap:10px}
.brand .dot{width:14px;height:14px;background:var(--orange)}
.brand.light{color:#fff}
.photo{position:absolute}
.headline{font-weight:800;font-size:38px;line-height:1.05;color:var(--navy);text-align:center;width:100%}
.headline .accent{color:var(--orange)}
.subline{font-weight:700;font-size:18px;color:var(--navy);text-align:center;width:100%;line-height:1.3}
.weblink{font-size:12px;font-weight:700;color:var(--navy);text-align:center;width:100%}
.contact{list-style:none;font-size:13px;line-height:1.2}
.contact li{display:flex;align-items:center;gap:10px;margin-bottom:10px}
.contact svg{flex:none}
.flap{position:absolute}
.topbar{position:absolute;left:0;top:26px;width:100%;height:34px;background:var(--navy)}
.topbar .label{position:absolute;left:0;top:0;height:34px;padding:0 34px 0 30px;background:var(--orange);color:#fff;font-weight:800;font-size:15px;line-height:34px;clip-path:polygon(0 0,100% 0,92% 100%,0 100%)}
.quote{color:var(--orange);font-weight:800;font-size:56px;line-height:.6}
.lead{font-weight:700;color:var(--navy);font-size:17px;line-height:1.25}
.lead.accent{color:var(--orange)}
.body{font-size:12px;line-height:1.55;color:var(--muted)}
.section-title{font-weight:800;font-size:26px;color:var(--navy)}
.section-title span{color:var(--orange)}
.services{list-style:none;font-size:12.5px;color:var(--ink);line-height:1.3}
.services li{display:flex;gap:10px;align-items:flex-start;margin-bottom:12px}
.services li::before{content:"";flex:none;width:8px;height:8px;margin-top:4px;background:var(--orange)}
.rule{position:absolute;height:3px;background:var(--orange)}
</style>
</head>
<body>

<!-- Outer spread: back (left) and front (right) -->
<section class="sheet outer-back" style="left:40px;top:300px;width:560px;height:792px">
  <div class="photo" role="img" aria-label="Foto: Straße mit Auto in blauem Licht" style="left:0;top:130px;width:560px;height:340px;background:linear-gradient(135deg,#3f6b8f,#9db6c9 55%,#1d3d5e)"></div>
  <svg class="abs" style="left:0;top:130px" width="560" height="340" viewBox="0 0 560 340">
    <polygon points="0,0 150,0 0,170" fill="#1d3d5e" opacity=".85"/>
    <polygon points="430,340 560,200 560,340" fill="#1d3d5e"/>
  </svg>
  <div class="brand abs" style="left:40px;top:560px;font-size:36px"><span>VERIDAX</span><span class="dot"></span></div>
  <ul class="contact abs" style="left:300px;top:540px">
    <li><svg width="16" height="16" viewBox="0 0 16 16"><path d="M8 1a5 5 0 0 0-5 5c0 4 5 9 5 9s5-5 5-9a5 5 0 0 0-5-5zm0 7a2 2 0 1 1 0-4 2 2 0 0 1 0 4z" fill="#f2a320"/></svg>Musterstraße 12</li>
    <li><svg width="16" height="16" viewBox="0 0 16 16"><path d="M8 1a5 5 0 0 0-5 5c0 4 5 9 5 9s5-5 5-9a5 5 0 0 0-5-5zm0 7a2 2 0 1 1 0-4 2 2 0 0 1 0 4z" fill="#f2a320"/></svg>10115 Berlin</li>
    <li><svg width="16" height="16" viewBox="0 0 16 16"><path d="M4 1l2 3-1.5 1.5a8 8 0 0 0 6 6L12 10l3 2-1.5 3C7 15 1 9 1 2.5z" fill="#f2a320"/></svg>0800 123 456</li>
    <li><svg width="16" height="16" viewBox="0 0 16 16"><rect x="1" y="3" width="14" height="10" fill="#f2a320"/><path d="M1 3l7 6 7-6" stroke="#fff" fill="none"/></svg>info@veridax-recht.de</li>
    <li><svg width="16" height="16" viewBox="0 0 16 16"><circle cx="8" cy="8" r="7" fill="#f2a320"/><path d="M1 8h14M8 1c3 3 3 11 0 14M8 1c-3 3-3 11 0 14" stroke="#fff" fill="none"/></svg>www.veridax-recht.de</li>
  </ul>
</section>

<section class="sheet outer-front" style="left:600px;top:300px;width:560px;height:792px">
  <div class="brand abs" style="left:0;width:560px;justify-content:center;top:48px;font-size:44px"><span>VERIDAX</span><span class="dot"></span></div>
  <div class="photo" role="img" aria-label="Foto: Mann sitzt neben beschädigtem roten Auto nach einem Unfall" style="left:0;top:140px;width:560px;height:330px;background:linear-gradient(120deg,#8a3b32,#b8a69a 50%,#6f7a82)"></div>
  <svg class="abs" style="left:0;top:140px" width="560" height="330" viewBox="0 0 560 330">
    <polygon points="390,0 560,0 560,330 470,330" fill="#f2a320"/>
    <polygon points="0,220 0,330 140,330" fill="#1d3d5e"/>
  </svg>
  <h1 class="headline abs" style="top:512px">PROFESSIONELLES<br><span class="accent">UNFALL–MANAGEMENT</span></h1>
  <p class="subline abs" style="top:610px">Die komplette Abwicklung Ihres<br>Verkehrsunfalles</p>
  <p class="weblink abs" style="top:690px">www.veridax-recht.de</p>
</section>

<!-- Pocket flaps -->
<svg class="flap" style="left:40px;top:1092px" width="1120" height="280" viewBox="0 0 1120 280">
  <polygon points="0,0 560,0 560,200 500,280 20,280 0,250" fill="#1d3d5e"/>
  <polygon points="560,0 1120,0 1120,250 1100,280 620,280 560,200" fill="#1d3d5e"/>
  <line x1="560" y1="0" x2="560" y2="200" stroke="#142c45" stroke-width="2"/>
</svg>
<div class="brand light abs" style="left:40px;width:560px;justify-content:center;top:1200px;font-size:30px"><span>VERIDAX</span></div>
<div class="brand light abs" style="left:600px;width:560px;justify-content:center;top:1200px;font-size:30px"><span>VERIDAX</span></div>

<!-- Inner spread -->
<section class="sheet inner-spread" style="left:40px;top:1660px;width:1120px;height:792px">
  <div class="topbar"><div class="label">PROFESSIONELLES UNFALL-MANAGEMENT</div></div>

  <div class="inner-left abs" style="left:0;top:0;width:560px;height:792px">
    <div class="quote abs" style="left:36px;top:100px">“</div>
    <p class="lead abs" style="left:80px;top:96px;width:430px">Verschwenden Sie kein teures Geld!</p>
    <p class="body abs" style="left:80px;top:126px;width:430px">Nach einem Unfall übernehmen wir die vollständige Regulierung mit der gegnerischen Versicherung. Sie tragen keine Kosten und sparen wertvolle Zeit.</p>
    <p class="lead accent abs" style="left:80px;top:206px;width:430px">Wir sind die Vertrauenswürdige Ihres Autohauses und helfen Ihnen gern</p>
    <p class="body abs" style="left:80px;top:260px;width:430px">Wir arbeiten eng mit Werkstätten und Gutachtern zusammen und sorgen für eine schnelle Auszahlung.</p>
    <div class="photo" role="img" aria-label="Foto: Auto auf einer Landstraße zwischen Bäumen" style="left:0;top:360px;width:560px;height:340px;background:linear-gradient(180deg,#c9d6cf,#7d9583 50%,#8c8f8e)"></div>
    <div class="brand abs" style="left:0;width:560px;justify-content:center;top:728px;font-size:26px"><span>VERIDAX</span><span class="dot" style="width:10px;height:10px"></span></div>
  </div>

  <div class="inner-right abs" style="left:560px;top:0;width:560px;height:792px">
    <h2 class="section-title abs" style="left:40px;top:92px">UNSER <span>SERVICE:</span></h2>
    <div class="rule" style="left:40px;top:130px;width:80px"></div>
    <ul class="services abs" style="left:40px;top:150px;width:230px">
      <li>Ihr direkter Ansprechpartner für alle Fragen</li>
      <li>Gutachten</li>
      <li>Reparaturkosten</li>
      <li>Nutzungsausfall</li>
      <li>Schmerzensgeld</li>
      <li>Mietwagenkosten</li>
      <li>Wertminderung</li>
      <li>Wir kümmern uns um sämtliche Formalitäten</li>
    </ul>
    <div class="quote abs" style="left:40px;top:470px">“</div>
    <p class="body abs" style="left:80px;top:462px;width:190px">Schnell, fair und transparent abgewickelt.</p>
    <p class="body abs" style="left:310px;top:96px;width:210px">Es ist wichtig, direkt nach dem Unfall anwaltlichen Rat einzuholen.</p>
    <p class="lead abs" style="left:310px;top:190px;width:210px;font-size:14px">Telefon: 0800 123 456</p>
    <div class="quote abs" style="left:310px;top:250px">“</div>
    <p class="body abs" style="left:350px;top:244px;width:170px">Unsere Beratung ist für Sie kostenlos.</p>
    <p class="body abs" style="left:310px;top:330px;width:210px">Tätig seit über 20 Jahren</p>
    <div class="photo" role="img" aria-label="Foto: beschädigter Wagen, hell und verblasst" style="left:0;top:520px;width:560px;height:190px;background:linear-gradient(180deg,#ffffff,#c9ced3 60%,#9aa2aa)"></div>
    <div class="brand abs" style="left:0;width:560px;justify-content:center;top:728px;font-size:26px"><span>VERIDAX</span><span class="dot" style="width:10px;height:10px"></span></div>
  </div>
</section>

</body>
</html>
```